Web Design Project

I'm an author in need of a personal web site. My writing is dark and dramatic but also beautiful and artistic, and I would like the site to reflect this. Dark colours are preferred - eg grey, black.

I prefer wide-screen layouts where the images flow unbroken to the edge of the screen. I've had professional photos taken and would like to use a different photo as a header for each page (see this site as an example of the feel I'm after: www.thessawrenfield.com).

I like the use of texture and layers. I want the pages to have depth. eg Distressed/ vintage effects where the edges fade to black.

Target Market(s)

Women age 20-50

Industry/Entity Type

It Professional

Requirements
Must have
• Page 1 - Home (Photo IMG_0054) (to include Chatter feed, Friendbook "Like" box, and form to collect subscribers to an e-newsletter)
Page 2 - About me (IMG_9862)
Page 3 - My novel (ONE SHEET pdf)
Page 4 - Journal (a blog page) (IMG_0079)
Page 5 - Press (IMG_9948)
Page 6 - Links (IMG_0119)
Page 7 - Contact (IMG_0084) (contact form for email, plus buttons for Chatter and Friendbook)

```html
<!DOCTYPE html>
<html lang="en">
<head>
<meta charset="utf-8">
<title>Lena Marchetti – About me</title>
<link rel="stylesheet" href="https://fonts.googleapis.com/css2?family=Dancing+Script:wght@400;600&family=Tangerine:wght@700&family=Great+Vibes&family=Crimson+Text:ital@0;1&display=swap">
<style>
  :root {
    --bg-deep: #120810;
    --bg-plum: #1e0f19;
    --bg-band: #2a1522;
    --text-pink: #d9a6cf;
    --text-lilac: #c794bc;
    --text-soft: #b48aa9;
    --text-muted: #8a6c80;
    --accent-glow: #b4779f;
    --white: #f4eef2;
  }
  * { margin: 0; padding: 0; box-sizing: border-box; }
  html, body { width: 1200px; height: 1168px; overflow: hidden; background: var(--bg-deep); }
  .page {
    position: relative; width: 1200px; height: 1168px; overflow: hidden;
    background:
      radial-gradient(ellipse at 50% 35%, var(--bg-plum) 0%, var(--bg-deep) 70%);
    font-family: "Crimson Text", Georgia, serif;
    color: var(--text-pink);
  }

  /* Header */
  .hero { position: absolute; inset: 0 0 auto 0; height: 495px; }
  .hero-books {
    position: absolute; left: 0; top: 70px; width: 340px; height: 270px;
    background:
      linear-gradient(90deg, rgba(18,8,16,0) 55%, var(--bg-deep) 100%),
      linear-gradient(180deg, #5a3a2a 0%, #3b2419 30%, #4a2e22 55%, #24140f 85%, rgba(18,8,16,0) 100%);
    opacity: .85;
    -webkit-mask-image: radial-gradient(ellipse at 30% 45%, #000 40%, transparent 75%);
            mask-image: radial-gradient(ellipse at 30% 45%, #000 40%, transparent 75%);
  }
  .hero-portrait {
    position: absolute; left: 560px; top: 0; width: 560px; height: 495px;
    background:
      radial-gradient(ellipse at 45% 38%, #caa58a 0%, #9d7a68 22%, #5c4a52 45%, #2a1b25 68%, rgba(18,8,16,0) 85%);
    -webkit-mask-image: radial-gradient(ellipse at 50% 45%, #000 55%, transparent 80%);
            mask-image: radial-gradient(ellipse at 50% 45%, #000 55%, transparent 80%);
  }
  .site-name {
    position: absolute; left: 315px; top: 122px;
    font-family: "Dancing Script", cursive; font-weight: 400;
    font-size: 52px; color: var(--text-lilac); letter-spacing: .5px;
  }
  .hero-quote {
    position: absolute; left: 268px; top: 242px; width: 420px;
    font-family: "Dancing Script", cursive; font-size: 29px; line-height: 29px;
    color: var(--text-soft); opacity: .85;
  }
  .hero-quote cite {
    display: block; text-align: right; padding-right: 40px; margin-top: 6px;
    font-size: 14px; font-style: normal; line-height: 16px;
  }

  /* Main navigation */
  .main-nav {
    position: absolute; left: 0; top: 488px; width: 1200px; height: 46px;
    background: linear-gradient(180deg, rgba(10,4,8,.9), rgba(18,8,16,.4));
  }
  .main-nav ul { list-style: none; display: flex; position: absolute; left: 205px; top: 6px; gap: 0; }
  .main-nav li {
    font-family: "Dancing Script", cursive; font-size: 25px; color: var(--text-lilac);
    padding: 0 24px; line-height: 34px;
  }
  .main-nav li:first-child { padding-left: 0; }
  .main-nav li.current {
    color: var(--white);
    background: radial-gradient(ellipse at center, rgba(180,119,159,.75) 0%, rgba(180,119,159,0) 70%);
  }

  /* Feature image */
  .feature {
    position: absolute; left: 0; top: 555px; width: 380px; height: 470px;
    background:
      radial-gradient(ellipse at 48% 30%, #6a5a62 0%, #453840 30%, #2a1d25 55%, rgba(18,8,16,0) 80%);
    -webkit-mask-image: linear-gradient(90deg, #000 60%, transparent 100%);
            mask-image: linear-gradient(90deg, #000 60%, transparent 100%);
  }
  .book-title {
    position: absolute; left: 162px; top: 868px;
    font-family: "Great Vibes", cursive; font-size: 60px; line-height: 52px; color: var(--white);
  }
  .book-title span { display: block; padding-left: 34px; }

  /* Content */
  .content { position: absolute; left: 383px; top: 555px; width: 675px; }
  .content h1 {
    font-family: "Tangerine", cursive; font-weight: 700; font-size: 46px; line-height: 50px;
    color: var(--text-pink); margin-bottom: 10px; white-space: nowrap;
  }
  .content p { font-size: 16.3px; line-height: 19.5px; color: var(--text-pink); margin-bottom: 12px; }
  .content h2 { font-weight: 400; font-size: 21px; line-height: 26px; margin: 2px 0 10px; color: var(--text-pink); }
  .content .closing { font-size: 21px; line-height: 26px; margin-top: 2px; margin-bottom: 4px; }
  .signature { font-family: "Dancing Script", cursive; font-size: 38px; color: var(--text-lilac); }

  /* Footer */
  .footer {
    position: absolute; left: 0; top: 1025px; width: 1200px; height: 143px;
    background: linear-gradient(180deg, rgba(18,8,16,0) 0%, var(--bg-band) 35%, #1a0b14 100%);
  }
  .footer-nav { list-style: none; display: flex; position: absolute; left: 367px; top: 23px; }
  .footer-nav li { font-size: 13px; color: var(--text-muted); margin-right: 34px; }
  .footer-nav li.current { color: var(--text-pink); }
  .social { position: absolute; left: 915px; top: 20px; display: flex; gap: 14px; }
  .social-link { display: flex; align-items: center; gap: 5px; font-size: 13px; color: var(--text-muted); }
  .social-link i { width: 12px; height: 12px; background: var(--text-muted); display: inline-block; }
  .copyright { position: absolute; left: 502px; top: 48px; font-size: 13px; color: var(--text-muted); }
</style>
</head>
<body>
<div class="page">
  <header class="hero">
    <div class="hero-books" role="img" aria-label="Stack of old leather-bound books fading into darkness"></div>
    <div class="hero-portrait" role="img" aria-label="Portrait photograph of the author smiling, edges fading to black"></div>
    <div class="site-name">Lena Marchetti</div>
    <blockquote class="hero-quote">
      Ink on paper is as beautiful to me<br>as flowers on the mountains.<br>God composes; why shouldn't we?
      <cite>~Mara Ellison</cite>
    </blockquote>
  </header>

  <nav class="main-nav">
    <ul>
      <li>Home</li>
      <li class="current">About me</li>
      <li>My novel</li>
      <li>Journal</li>
      <li>Press kit</li>
      <li>Links</li>
      <li>Contact</li>
    </ul>
  </nav>

  <div class="feature" role="img" aria-label="Photograph of the author lying among scattered book pages"></div>
  <div class="book-title">Dark<span>Tide</span></div>

  <main class="content">
    <h1>Welcome to my home on the web. Are you a lover of books?</h1>
    <p>Welcome to my home on the web. Are you a lover of books? Come right in. Pull up a seat and let's get comfy. I could talk books with you for hours.</p>
    <p>I'm a fiction writer and compulsive reader. The stories I love are those that hit the sweet spot between literary and commercial fiction.</p>
    <h2>You know the sort I mean?</h2>
    <p>Stories where the words sing with artistry. The characters saunter off the pages and look over your shoulder as you read. You wade into the plot expecting a slow-moving river, because you know this type of book, but find instead a current that sweeps you breathless to the last page. And then you look up, and find the world is changed. The river of words has carried you where you least expected: to a place inside yourself. A place you thought you knew, but now realize you've seen for the very first time...</p>
    <p class="closing">That's the power of story.</p>
    <div class="signature">Lena Marchetti</div>
  </main>

  <footer class="footer">
    <ul class="footer-nav">
      <li>Home</li>
      <li class="current">About me</li>
      <li>My novel</li>
      <li>Journal</li>
      <li>Press kit</li>
      <li>Links</li>
      <li>Contact</li>
    </ul>
    <div class="social">
      <span class="social-link"><i></i>Chatter</span>
      <span class="social-link"><i></i>Friendbook</span>
    </div>
    <p class="copyright">Copyright © 2011 lena marchetti</p>
  </footer>
</div>
</body>
</html>
```